Curantel System Web Page Design

This project is to design 6 pages of a web based medical system for clinics, hospitals, drugs suppliers, general items suppliers, insurance company, laboratories and patients (basically all parties which could be involved in).We want the designs of the browser, button, icon and layout are based on Oru, which is user friendly, looks professional, simple and neat but with powerful functions. We have uploaded few pictures of another system, please do not copy its design because this is not what we are looking for, the pictures are for you to know the elements should be included in our pages. Curantel web-base system, design 6 pages1. Login PageShould include the following elements-company id with input field-login id with input field-password with input field2. Main Page (Navigation page)Should include the following elements-Appointment-Consultation-Patient-Drugs inventory -General supplies inventory -Laboratory-Suppliers-Insurance-Reports 3. Appointment PageShould include all the the elements in the respective pictures plus the followings-Daily View, Weekly View, Monthly View buttons4. Consultation PageShould include all the the elements in the respective picture5. Patient Page5.1 General information Should include all the the elements in the respective picture5.2 medical history/lab reportsShould include all the the elements in the respective picture plus the followings-Notify patient button-Share report button.
Please stop using Ward Harbor in your designs which is not the name of our system. We have just rename our system to Curantel, please take note.
We need the system to look professional not playful, do not use too many colors and playful icons.
professional users
5+ page

```html
<!DOCTYPE html>
<html lang="en">
<head>
<meta charset="utf-8">
<title>Curantel – Home</title>
<link href="https://fonts.googleapis.com/css2?family=Raleway:wght@400;500;600&display=swap" rel="stylesheet">
<style>
:root{
  --brand:#3b66e6;
  --text-blue:#3f63d6;
  --icon:#2dcb8c;
  --bg:#ffffff;
  --header-line:#eef1f7;
  --card-shadow:rgba(20,30,60,.16);
  --muted:#333a45;
}
*{box-sizing:border-box;margin:0;padding:0}
html,body{width:1200px;height:675px;overflow:hidden;background:var(--bg)}
body{font-family:"Raleway",sans-serif;position:relative}
.topbar{position:absolute;left:0;top:0;width:1200px;height:44px;border-bottom:1px solid var(--header-line);box-shadow:0 2px 6px rgba(40,60,120,.05)}
.brand{position:absolute;left:50px;top:10px;font-size:20px;font-weight:500;color:var(--brand);line-height:24px}
.account{position:absolute;right:47px;top:8px;height:28px;display:flex;align-items:center;white-space:nowrap}
.lang{display:flex;align-items:center;gap:4px;font-size:10px;color:var(--brand);font-weight:500;margin-right:15px}
.profile{display:flex;align-items:center;gap:7px;font-size:13px;color:var(--brand)}
.avatar{width:28px;height:28px;border-radius:50%;flex:none;background:linear-gradient(135deg,#d9b49a,#6a4c3f)}
.profile svg{margin-left:6px}
.grid{position:absolute;left:149px;top:129px;display:grid;grid-template-columns:repeat(3,255px);grid-auto-rows:105px;column-gap:68px;row-gap:32px}
.tile{background:#fff;box-shadow:0 2px 6px var(--card-shadow);display:flex;align-items:center;padding-left:29px;text-decoration:none}
.tile svg{width:32px;height:32px;flex:none;fill:none;stroke:var(--icon);stroke-width:1.4;stroke-linecap:round;stroke-linejoin:round}
.tile span{margin-left:24px;font-size:15.5px;color:var(--text-blue);letter-spacing:.2px;white-space:nowrap}
.helpline{position:absolute;left:0;width:1200px;top:641px;text-align:center;font-size:10px;color:var(--muted)}
.helpline a{color:var(--brand);text-decoration:none}
</style>
</head>
<body>
<header class="topbar">
  <div class="brand">Curantel.</div>
  <div class="account">
    <div class="lang">
      <svg width="13" height="13" viewBox="0 0 14 14" fill="none" stroke="currentColor" stroke-width="1.2"><circle cx="7" cy="7" r="6"/><ellipse cx="7" cy="7" rx="2.6" ry="6"/><path d="M1 7h12"/></svg><span>EN</span>
    </div>
    <div class="profile">
      <div class="avatar" role="img" aria-label="Profile photo of the signed-in administrator"></div>
      <span>Dana Whitlow</span>
      <svg width="10" height="10" viewBox="0 0 10 10" fill="none" stroke="currentColor" stroke-width="1.4"><path d="M2 4l3 3 3-3"/></svg>
    </div>
  </div>
</header>

<main class="grid">
  <a class="tile" href="#"><svg viewBox="0 0 32 32"><rect x="4" y="6" width="24" height="22" rx="1"/><path d="M4 11h24M10 4v4M22 4v4"/><path d="M8 15h3v3H8zM14 15h3v3h-3zM20 15h3v3h-3zM8 21h3v3H8zM14 21h3v3h-3zM20 21h3v3h-3z"/></svg><span>Appointment</span></a>
  <a class="tile" href="#"><svg viewBox="0 0 32 32"><circle cx="16" cy="10" r="5"/><path d="M11 8h10"/><path d="M5 29v-4c0-4 4-7 11-7s11 3 11 7v4z"/><path d="M11 18v5a2 2 0 0 0 4 0M21 18v6"/><circle cx="21" cy="26" r="1.6"/></svg><span>Consultation</span></a>
  <a class="tile" href="#"><svg viewBox="0 0 32 32"><circle cx="16" cy="10" r="6"/><path d="M10 8h12"/><path d="M5 29v-4c0-5 5-8 11-8s11 3 11 8v4z"/></svg><span>Patient</span></a>
  <a class="tile" href="#"><svg viewBox="0 0 32 32"><rect x="6" y="3" width="20" height="24" rx="1"/><path d="M6 27v2h20"/><rect x="10" y="7" width="12" height="11"/><path d="M16 9v7M12.5 12.5h7M13 22h6"/></svg><span>Drugs Inventory</span></a>
  <a class="tile" href="#"><svg viewBox="0 0 32 32"><rect x="6" y="3" width="20" height="24" rx="1"/><path d="M6 27v2h20"/><rect x="10" y="7" width="12" height="11"/><path d="M13 22h6"/></svg><span>General Supplies</span></a>
  <a class="tile" href="#"><svg viewBox="0 0 32 32"><path d="M5 28h20M9 25h12"/><path d="M14 25c-5-1-6-7-2-10"/><rect x="15" y="6" width="5" height="11" rx="1" transform="rotate(25 17 11)"/><path d="M19 3l3 1.5M21 17l3 1M23 17v5"/></svg><span>Laboratory</span></a>
  <a class="tile" href="#"><svg viewBox="0 0 32 32"><path d="M3 23v-8l4-5h8v13"/><rect x="15" y="7" width="14" height="16"/><path d="M22 11v8M18 15h8M3 17h8"/><circle cx="8" cy="25" r="2.5"/><circle cx="23" cy="25" r="2.5"/></svg><span>Suppliers</span></a>
  <a class="tile" href="#"><svg viewBox="0 0 32 32"><path d="M16 28L5 17a6.5 6.5 0 0 1 11-7 6.5 6.5 0 0 1 11 7z"/><path d="M16 13v8M12 17h8"/></svg><span>Insurance</span></a>
  <a class="tile" href="#"><svg viewBox="0 0 32 32"><path d="M10 3h12l5 5v18H10z"/><path d="M22 3v5h5"/><path d="M5 8h10l4 4v17H5z"/><path d="M10 14v5M7.5 16.5h5M8 22h8M8 25h8"/></svg><span>Reports</span></a>
</main>

<footer class="helpline">24/7 Helpline: <a href="#">+100 555 0142</a></footer>
</body>
</html>
```